RPM/CCM Marketing Book

We need a new logo designed for the company,
Bramford Diagnostics, some logo ideas are attached.

We would like this book revamped with a new design as well as included updates made in line with the design and text. Please let me know of any clarifications or follow-up questions that possible can come up. The old booklet is attached as well which is to be used for the new design.

```html
<!DOCTYPE html>
<html lang="en">
<head>
<meta charset="utf-8">
<title>Bramford Diagnostics – RPM/CCM Marketing Book</title>
<link href="https://fonts.googleapis.com/css2?family=Roboto:ital,wght@0,400;0,500;0,700;1,400&family=Roboto+Condensed:wght@400;700&display=swap" rel="stylesheet">
<style>
:root{
  --blue:#29abe2;
  --blue-dark:#1d8fc8;
  --blue-light:#cdeaf8;
  --gray:#7d7f82;
  --gray-dark:#5e6064;
  --ink:#4d4f53;
  --board:#48484a;
  --orange:#f7941d;
  --white:#ffffff;
  --paper:#f4f5f6;
}
html,body{margin:0;width:913px;height:1200px;overflow:hidden;background:var(--board)}
.board{position:relative;width:913px;height:1200px;font-family:Roboto,sans-serif;color:var(--ink)}
.spread{position:absolute;width:418px;height:271px;background:var(--white);overflow:hidden}
.a{position:absolute}
.cond{font-family:'Roboto Condensed',sans-serif;font-weight:700}
.tiny{font-size:3.2px;line-height:1.4}
.small{font-size:3.7px;line-height:1.4}
.white{color:var(--white)}
.blue{color:var(--blue)}
.bg-blue{background:var(--blue)}
.bg-gray{background:var(--gray)}
.brand{display:flex;align-items:center;gap:2px;font-weight:700;font-size:4px;color:var(--blue);white-space:nowrap}
.brand i{display:block;width:5px;height:5px;background:var(--blue)}
.brand.on-dark{color:var(--white)}
.brand.on-dark i{background:var(--white)}
.site-head{position:absolute;top:12px;right:12px;display:flex;align-items:center;gap:5px;font-size:3px}
.site-head span{color:var(--gray)}
.site-head.on-dark span{color:var(--white)}
.folio{position:absolute;bottom:0;width:4px;height:11px;background:var(--blue)}
.folio.l{left:7px}.folio.r{right:7px}
.title{font-family:'Roboto Condensed',sans-serif;font-weight:700;font-size:14px;line-height:1;color:var(--blue);margin:0}
ul,ol{margin:0;padding:0}
.dots li{list-style:none;position:relative;padding-left:4px}
.dots li::before{content:"";position:absolute;left:0;top:1.6px;width:1.3px;height:1.3px;border-radius:50%;background:currentColor}
/* cover */
.cover-logo{left:19px;top:21px;width:63px;height:42px;border:1.5px solid var(--white);box-sizing:border-box;background:rgba(255,255,255,.95);display:flex;align-items:center;justify-content:center}
.service-band{left:209px;top:213px;width:209px;height:37px;background:var(--blue);text-align:center;color:var(--white)}
.service-band p{margin:0}
/* toc */
.toc{left:296px;top:49px;width:116px;font-size:3.2px;color:var(--white)}
.toc li{list-style:none;display:flex;justify-content:space-between;line-height:6.4px}
.toc .main{color:#bfe7fb;font-weight:500;margin-top:2.5px}
.toc .sub{padding-left:6px}
/* compare table */
.compare{left:0;top:104px;width:197px;display:grid;grid-template-columns:1fr 1fr;font-size:3px;line-height:1.35}
.compare div{padding:1.5px 3px;border-bottom:.4px solid var(--white);border-right:.4px solid var(--white)}
.compare .hd{background:var(--blue-dark);color:var(--white);font-size:4.3px;font-weight:500}
.compare .lt{background:var(--blue-light)}
.compare .bl{background:var(--blue);color:var(--white)}
.compare .full{grid-column:1/3;background:var(--blue-light);display:grid;grid-template-columns:1fr 1fr;gap:0 4px}
/* numbered steps */
.steps{font-size:3.2px;line-height:1.38;color:var(--gray-dark)}
.steps li{list-style:none;display:flex;gap:3px;margin-bottom:3.4px}
.steps b{font-weight:400;min-width:5px}
/* benefit items */
.benefit{display:flex;gap:4px;margin-bottom:5px}
.benefit i{flex:none;width:8px;height:8px;border-radius:50%;background:var(--white);display:block}
.benefit p{margin:0;font-size:3px;line-height:1.35;color:var(--white)}
.benefit strong{display:block;font-size:3.3px}
.info-icon{width:8px;height:8px;border:.6px solid var(--white);border-radius:50%;color:var(--white);font-size:5px;line-height:8px;text-align:center;box-sizing:border-box;font-family:serif;font-style:italic}
/* care plan */
.plan-item{display:flex;gap:6px;align-items:flex-start;margin-bottom:6px;font-size:3.1px;line-height:1.4;color:var(--gray-dark)}
.plan-item i{flex:none;width:9px;height:9px;border:.8px solid var(--blue);border-radius:2px;display:block;box-sizing:border-box}
/* code table */
.codes{left:232px;top:109px;width:165px;border-collapse:collapse;font-size:2.9px;line-height:1.3;background:var(--white);color:var(--ink)}
.codes th{background:var(--blue);color:var(--white);font-weight:500;font-size:3.8px;padding:2px 1px;border:.4px solid var(--white)}
.codes td{border:.4px solid var(--blue);padding:1.5px 1.5px;vertical-align:middle}
.codes td:first-child,.codes td:nth-child(2),.codes td:last-child{text-align:center}
.codes ul li{list-style:none;position:relative;padding-left:3px}
.codes ul li::before{content:"";position:absolute;left:0;top:1.3px;width:1.1px;height:1.1px;border-radius:50%;background:var(--ink)}
/* patient scenario tables */
.scenario{position:absolute;background:var(--white);border:.5px solid var(--blue);font-size:2.8px;line-height:1.35;color:var(--ink)}
.scenario.orange{border-color:var(--orange)}
.scenario .bar{background:var(--blue);color:var(--white);text-align:center;font-size:3.6px;padding:2.2px 0;letter-spacing:.1px}
.scenario.orange .bar{background:var(--orange)}
.scenario .desc{font-style:italic;text-align:center;padding:2px 8px;font-size:3.1px;color:var(--gray-dark)}
.scenario .cols{display:grid;grid-template-columns:1fr 46px;color:var(--blue);font-size:3.6px;padding:1px 4px;border-bottom:.4px solid var(--blue)}
.scenario .cols span::before{content:"";display:inline-block;width:3.4px;height:3.4px;border-radius:50%;background:var(--blue);margin-right:2px;vertical-align:-.4px}
.scenario .row{display:grid;grid-template-columns:1fr 46px 7px;border-bottom:.35px solid #d6dadd;align-items:center}
.scenario .row>div{padding:1.4px 3px}
.scenario .row .t{display:flex;align-items:center;gap:2px;border-left:.35px solid #d6dadd}
.scenario .row .t::before{content:"✓";display:block;width:3.4px;height:3.4px;border-radius:50%;background:var(--blue);color:var(--white);font-size:2.6px;line-height:3.4px;text-align:center;flex:none}
.scenario .row .t.no::before{content:"✕";background:var(--orange)}
.scenario .row.bill{color:var(--blue)}
.scenario .row.bill .t{background:var(--blue);color:var(--white)}
.scenario .row.bill .t::before{background:var(--white);color:var(--blue)}
.scenario .row .m{font-size:2px;color:var(--blue);text-align:center;line-height:1;writing-mode:vertical-rl;transform:rotate(180deg)}
.scenario .note{font-size:2.3px;padding:1px 4px;color:var(--gray-dark);border-bottom:.35px solid #d6dadd}
</style>
</head>
<body>
<main class="board">

<!-- ===== Row 1 : Cover ===== -->
<section class="spread" style="left:35px;top:26px">
  <div class="a bg-blue" style="left:0;top:0;width:209px;height:210px"></div>
  <div class="a" role="img" aria-label="Faint photo of a tablet showing health data" style="left:0;top:0;width:209px;height:210px;background:linear-gradient(135deg,rgba(255,255,255,.08),rgba(20,110,170,.25))"></div>
  <div class="a cover-logo"><div class="brand"><i></i>Bramford Diagnostics</div></div>
  <p class="a" style="left:26px;top:247px;margin:0;font-size:5.6px;color:var(--gray-dark)">www.bramforddx.com</p>
  <div class="a" role="img" aria-label="Photo of a doctor with a patient holding a laptop" style="left:209px;top:0;width:209px;height:216px;background:linear-gradient(160deg,#c9ccd0,#8e9398 70%,#6f7377)"></div>
  <div class="a service-band">
    <p class="cond" style="font-size:7.4px;margin-top:8px;letter-spacing:.2px">RPM · CCM · RTM · CPM · BHI · TCM · PCM</p>
    <p style="font-size:8px;margin-top:3px">2023</p>
  </div>
  <p class="a" style="left:209px;width:209px;top:253px;margin:0;text-align:center;font-size:5.6px;font-weight:700;color:var(--gray-dark)">www.bramforddx.com</p>
</section>

<!-- ===== Row 1 : Table of contents ===== -->
<section class="spread bg-gray" style="left:470px;top:26px">
  <div class="a" role="img" aria-label="Photo of three medical professionals reviewing a clipboard" style="left:0;top:0;width:230px;height:271px;background:linear-gradient(120deg,#e9ebed,#c7cbcf 55%,#9aa0a6);clip-path:polygon(0 0,100% 0,86% 100%,0 100%)"></div>
  <div class="site-head on-dark"><span>www.bramforddx.com</span><div class="brand on-dark"><i></i>Bramford Diagnostics</div></div>
  <h2 class="a white" style="left:231px;top:47px;margin:0;font-family:'Roboto Condensed',sans-serif;font-weight:400;font-size:10px;line-height:1.05">TABLE OF<br>CONTENTS</h2>
  <ul class="a toc">
    <li class="main"><span>1. The case for doing monitoring in-house.</span><span>1</span></li>
    <li class="main"><span>2. How to Get Started</span><span>2</span></li>
    <li class="main"><span>3. Chronic Care Management (CCM)</span><span>3</span></li>
    <li class="sub"><span>a. Who can perform CCM</span><span>4</span></li>
    <li class="sub"><span>b. CCM Results</span><span>4</span></li>
    <li class="sub"><span>c. Who is Eligible for CCM</span><span>5</span></li>
    <li class="sub"><span>d. CCM Care Plan</span><span>6</span></li>
    <li class="sub"><span>e. Classic vs Complex CCM</span><span>8</span></li>
    <li class="sub"><span>f. CCM CPT Codes</span><span>8</span></li>
    <li class="sub"><span>g. CCM Patient Scenarios</span><span>9</span></li>
    <li class="main"><span>4. Remote Patient Monitoring (RPM)</span><span>12</span></li>
    <li class="sub"><span>a. Featured Equipment</span><span>12</span></li>
    <li class="sub"><span>b. Benefits of RPM</span><span>15</span></li>
    <li class="sub"><span>c. RPM Requirements</span><span>16</span></li>
    <li class="sub"><span>d. RPM Benefits for Patients with Chronic Conditions</span><span>18</span></li>
    <li class="sub"><span>e. RPM Benefits for Patients with Diabetes</span><span>19</span></li>
    <li class="sub"><span>f. RPM Use for Chronic Conditions</span><span>20</span></li>
    <li class="sub"><span>g. Telehealth &amp; RPM in Diabetes Care</span><span>21</span></li>
    <li class="sub"><span>h. Remote Monitoring for High Blood Pressure</span><span>24</span></li>
    <li class="sub"><span>i. RPM Key Features of the Program</span><span>27</span></li>
    <li class="sub"><span>j. RPM CPT Codes</span><span>29</span></li>
    <li class="main"><span>5. Potential Revenue</span><span>30</span></li>
    <li class="sub"><span>a. RPM Revenue</span><span>30</span></li>
    <li class="sub"><span>b. CCM Revenue</span><span>32</span></li>
  </ul>
  <div class="folio l"></div><div class="folio r"></div>
</section>

<!-- ===== Row 2 : Case for outsourcing / How to get started ===== -->
<section class="spread" style="left:35px;top:317px">
  <div class="a bg-gray" style="left:0;top:0;width:197px;height:104px"></div>
  <div class="a brand on-dark" style="left:18px;top:47px;font-size:3.8px"><i></i>Kestrel Care, LLC</div>
  <h2 class="a white cond" style="left:19px;top:64px;margin:0;font-size:13px">The Case for <span class="blue">Outsourcing</span></h2>
  <p class="a white" style="left:19px;top:84px;margin:0;font-size:5px;font-weight:700;line-height:1.25">Remote Patient Monitoring/Chronic Care Management<br>to a trusted 3rd party Kestrel Care, LLC</p>
  <div class="a compare">
    <div class="hd">CCM</div><div class="hd">RPM</div>
    <div class="lt">24/7 Access call center. Kestrel Care acts as an extension of your care coordination team so your patients with chronic conditions have access to a clinician, 24/7.</div>
    <div class="lt">Monitoring program collects wide range of health data from the point of care: vital signs, weight, blood pressure, blood sugar, blood oxygen, heart rate and electrocardiograms.</div>
    <div class="bl">Certified Medical Staff</div><div class="bl">Certified Medical Staff</div>
    <div class="lt">Kestrel Care will develop a comprehensive care plan per Medicare regulations for CCM.</div>
    <div class="lt">Equipment works on Cellular network, no need for patient to have internet service.</div>
    <div class="bl">Facilitating communication between all of health-care providers and patients.</div>
    <div class="bl">Installation and Ordering of RPM Equipment and Setting up the equipment in patients home.</div>
    <div class="full"><span style="grid-column:1/3;font-weight:500;margin-bottom:2px">MONTHLY CALLS INCLUDE:</span>
      <span>1. Review of medications<br>2. Discussion of test results<br>3. Exercise and therapy options<br>4. Scheduling regular or unanticipated office visits with the primary provider</span>
      <span>5. Referrals to specialists, as needed<br>6. Provide Education on the patients Chronic Conditions</span></div>
  </div>
  <p class="a" style="left:19px;top:205px;margin:0;font-size:5.4px;font-weight:700;color:var(--ink)"><span class="blue">MEDICAL</span> Offices Benefits:</p>
  <ul class="a dots small" style="left:22px;top:216px;width:180px;color:var(--gray-dark);font-size:3.5px;line-height:1.35">
    <li>Keep your workflow No Staff, No Space or Scheduling from your staff needed</li>
    <li>Reduce scheduling burden from front office</li>
    <li>Immediate Revenue</li>
    <li>New Income Stream</li>
    <li>Improve your MIPS Score</li>
    <li>Able to provide Telemedicine Visits on patients who are participating in Kestrel Care RPM/CCM program</li>
    <li>Increase Patient Satisfaction</li>
  </ul>
  <div class="a" role="img" aria-label="Photo of a patient talking with a doctor across a desk" style="left:212px;top:104px;width:117px;height:95px;background:linear-gradient(135deg,#d9dde1,#a3a9ae 60%,#7d848a)"></div>
  <div class="site-head"><span>www.bramforddx.com</span><div class="brand"><i></i>Bramford Diagnostics</div></div>
  <h2 class="a title" style="left:239px;top:32px">How to Get Started:</h2>
  <ol class="a steps" style="left:240px;top:52px;width:80px">
    <li><b>1.</b>Practice discusses with patient if Patient is interested in RPM and/or CCM program.</li>
    <li><b>2.</b>Practice by fax or online intake submits an initial order for RPM and/or CCM with the patient H&amp;P.</li>
    <li><b>3.</b>We will contact each patient on your behalf and explain the CCM and RPM program.</li>
    <li><b>4.</b>The patient must opt into CCM and RPM program by signing a consent.</li>
  </ol>
  <ol class="a steps" style="left:332px;top:52px;width:76px">
    <li><b>5.</b>The patient can also opt out of the program at any time, at the end of the calendar month.</li>
    <li><b>6.</b>We will go to patients' home explain and educate on the program and obtain the signature on the consent forms.</li>
    <li><b>7.</b>We will order and install all the equipment in the patient's home.</li>
    <li><b>8.</b>RPM/CCM services are done under Prescribing Physician General Supervision, see CMS definitions below.</li>
    <li><b>9.</b>Only the prescribing physician can bill for the RPM/CCM Service.</li>
    <li><b>10.</b>Kestrel Care can bill for CCM/RPM directly on physician behalf.</li>
    <li><b>11.</b>The required time for RPM/CCM will be documented in the EHR system of Kestrel Care.</li>
    <li><b>12.</b>The EHR System is cloud based and the Physician shall have complete access to his patient charts.</li>
    <li><b>13.</b>At Physician discretion Kestrel Care can upload and document encounters in the Physician current EHR system for staff review.</li>
  </ol>
  <div class="a bg-blue" style="left:209px;top:207px;width:209px;height:64px"></div>
  <p class="a white" style="left:219px;top:213px;width:86px;margin:0;font-size:2.4px;line-height:1.4">* CCM and RPM qualify as designated care management services under 42 CFR 410.26(b)(5), meaning these services can be furnished under general supervision of the billing practitioner.<br><br>Billing practitioner may arrange to have clinical staff external to the practice provide care management services for his or her patients, if all requirements for incident to billing are satisfied.</p>
  <p class="a white" style="left:312px;top:213px;width:86px;margin:0;font-size:2.4px;line-height:1.4">Clinical Staff: a person who works under the supervision of a physician or other qualified health professional and who is allowed by law and facility policy to perform or assist in a professional service.<br><br>General Supervision: the service is furnished under overall direction and control of the physician, whose presence is not required, and who is available by telephone.</p>
  <div class="folio l"></div><div class="folio r"></div>
</section>

<!-- ===== Row 2 : Chronic Care Management ===== -->
<section class="spread" style="left:470px;top:317px">
  <div class="a bg-gray" style="left:0;top:0;width:209px;height:271px"></div>
  <div class="a" role="img" aria-label="Photo of a physician in a white coat holding a stethoscope" style="left:0;top:0;width:92px;height:271px;background:linear-gradient(90deg,#f1f2f3,#d3d6d9 70%,#9da2a7)"></div>
  <h2 class="a title" style="left:38px;top:31px;font-size:13.5px">Chronic Care Management</h2>
  <div class="a white" style="left:94px;top:54px;width:106px;text-align:center">
    <p style="margin:0;font-size:6px">Overview</p>
    <p style="margin:6px 0 2px;font-size:5.5px;font-weight:500">What is Chronic Care Management?</p>
    <p class="tiny" style="margin:0">Chronic Care Management (CCM) offers personal support to patients with complex needs. This added level of care and service leads patients to a healthier lifestyle by proactively managing their care and providing a trusted clinical resource they can reach around-the-clock.</p>
    <p class="tiny" style="margin:3px 0 0">CCM is designed for patients with two or more chronic conditions that are anticipated to last at least 12 months or until the patient's death.</p>
    <p class="tiny" style="margin:3px 0 0">Patients enrolled in CCM services benefit from an entire care team focused on their needs, increased communication with their provider and improved care coordination.</p>
    <p style="margin:8px 0 2px;font-size:6px;font-weight:500">CCM Benefits</p>
    <p class="tiny" style="margin:0">Two thirds of patients on Medicare have two or more chronic conditions, which means many patients can benefit from CCM services. CCM can help your clinic deliver coordinated care to patients that need additional time and resources between appointments.</p>
  </div>
  <div class="a" style="left:102px;top:178px;width:100px">
    <div class="benefit"><i></i><p><strong>Better Patient Outcomes</strong>Patients gain a supportive healthcare team dedicated to creating a comprehensive care plan.</p></div>
    <div class="benefit"><i></i><p><strong>Improved Patient Satisfaction</strong>Patient care is focused on prevention to keep patients out of the hospital by supporting patients between visits.</p></div>
    <div class="benefit"><i></i><p><strong>Improved Care Coordination</strong>Referral coordination helps keep patients out of the hospital and prevents patients from "falling through the cracks."</p></div>
    <div class="benefit"><i></i><p><strong>Increased Revenue</strong>CCM Increases Income for the clinic by billing CCM services.</p></div>
  </div>
  <div class="a bg-blue" style="left:209px;top:0;width:209px;height:62px"></div>
  <div class="site-head on-dark"><span>www.bramforddx.com</span><div class="brand on-dark"><i></i>Bramford Diagnostics</div></div>
  <div class="a info-icon" style="left:229px;top:42px"></div>
  <p class="a white" style="left:242px;top:42px;width:150px;margin:0;font-size:3.1px;font-style:italic;line-height:1.35">Chronic Care Management (CCM) is a new Medicare program that offers significant monthly reimbursement for the time providers and their staff spend helping patients between office visits.</p>
  <p class="a" style="left:232px;top:74px;margin:0;font-size:6px;font-weight:500;color:var(--gray-dark)">Who Can Perform CCM Services?</p>
  <ul class="a dots tiny" style="left:235px;top:90px;width:95px;color:var(--gray-dark);line-height:1.9">
    <li>Registered Nurses (RNs)</li><li>Licensed Practical Nurses (LPNs)</li><li>Medical Assistants (MAs)</li><li>Medical Doctors (MDs) or Doctors of Osteopathic Medicine (DOs)</li><li>Physician Assistant - Certified (PA-Cs)</li><li>Advanced Practice Registered Nurses (APRNs)</li><li>Contracted third party vendors</li>
  </ul>
  <div class="a" role="img" aria-label="Photo of a nurse in blue scrubs holding a clipboard" style="left:335px;top:74px;width:50px;height:60px;background:linear-gradient(180deg,#eef3f6,#9fcbe6)"></div>
  <p class="a tiny" style="left:232px;top:148px;width:96px;margin:0;font-size:2.7px;color:var(--gray-dark)">In 2015, The Centers for Medicare &amp; Medicaid Services (CMS) unveiled a new code, <u class="blue">CPT 99490 - Chronic Care Management Services</u>, that reimburses primary care providers and chronic disease specialists for 20+ minutes of non-face-to-face clinical staff time spent on care coordination for Medicare patients with multiple chronic conditions. CMS studies have confirmed that CCM contributes to better outcomes and higher patient satisfaction. Therefore, CMS has since expanded the program to include 6 billing codes that offer <u class="blue">$42-$139+ per patient per month.</u></p>
  <p class="a blue" style="left:335px;top:148px;margin:0;font-size:3.6px;line-height:1.25">Chronic Care Management<br>results:*</p>
  <ul class="a dots tiny" style="left:337px;top:158px;color:var(--gray-dark);line-height:1.7"><li>5.6% Hospitalizations</li><li>4.2% ER visits</li><li>+70% ROI for CMS</li></ul>
  <p class="a blue" style="left:335px;top:183px;width:70px;margin:0;font-size:3.4px;line-height:1.25">CCM reimbursement is steadily increasing while E/M visit reimbursement is declining:</p>
  <svg class="a" style="left:335px;top:199px" width="66" height="44" viewBox="0 0 66 44" role="img" aria-label="Line chart of CCM versus office visit reimbursement 2011 to 2020">
    <g stroke="#d5d8db" stroke-width=".3"><line x1="6" y1="4" x2="64" y2="4"/><line x1="6" y1="10" x2="64" y2="10"/><line x1="6" y1="16" x2="64" y2="16"/><line x1="6" y1="22" x2="64" y2="22"/><line x1="6" y1="28" x2="64" y2="28"/></g>
    <polyline points="6,13 13,14 20,14 27,15 34,16 41,16 48,17 55,18 62,19" fill="none" stroke="#e8492f" stroke-width=".7"/>
    <polyline points="34,24 41,20 48,14 55,10 62,6" fill="none" stroke="var(--blue)" stroke-width=".7"/>
    <polyline points="48,16 55,12 62,9" fill="none" stroke="var(--orange)" stroke-width=".7"/>
    <g font-size="2" fill="#8a8d91" font-family="Roboto,sans-serif"><text x="0" y="5">$300</text><text x="0" y="17">$150</text><text x="0" y="29">$0</text><text x="6" y="33">2011  2013  2015  2017  2019</text></g>
    <g font-size="1.8" fill="#8a8d91" font-family="Roboto,sans-serif"><rect x="6" y="38" width="2" height="2" fill="var(--orange)"/><text x="9" y="40">CPT 99487</text><rect x="24" y="38" width="2" height="2" fill="#e8492f"/><text x="27" y="40">E/M 99214</text><rect x="42" y="38" width="2" height="2" fill="var(--blue)"/><text x="45" y="40">CPT 99490</text></g>
  </svg>
  <p class="a blue" style="left:232px;top:204px;width:96px;margin:0;font-size:3.5px;line-height:1.25">CCM enables billing for previously unreimbursed activities such as:</p>
  <ul class="a dots tiny" style="left:234px;top:215px;width:46px;color:var(--gray-dark);font-size:2.8px"><li>making phone calls</li><li>answering questions</li><li>triaging symptoms</li><li>refilling medication</li><li>reviewing lab results</li><li>scheduling appointments</li><li>coordinating referrals</li><li>care planning</li></ul>
  <ul class="a dots tiny" style="left:283px;top:215px;width:46px;color:var(--gray-dark);font-size:2.8px"><li>reviewing charts</li><li>arranging transportation</li><li>following up with patients</li><li>managing overall patient care</li></ul>
  <div class="folio l"></div><div class="folio r"></div>
</section>

<!-- ===== Row 3 : Eligibility / Care plan ===== -->
<section class="spread" style="left:35px;top:607px">
  <div class="a bg-blue" style="left:0;top:0;width:298px;height:271px"></div>
  <h2 class="a white cond" style="left:17px;top:48px;margin:0;font-size:14px">Who is Eligible?</h2>
  <p class="a white tiny" style="left:17px;top:76px;width:100px;margin:0">If you live with two or more chronic conditions, CCM can help you manage your care. Some examples of chronic conditions include, but are not limited to:</p>
  <ul class="a dots white tiny" style="left:17px;top:96px;width:55px;line-height:2.3"><li>Alzheimer's and Related Dementia</li><li>Arthritis</li><li>Asthma</li><li>Cancer</li><li>COPD</li></ul>
  <ul class="a dots white tiny" style="left:78px;top:96px;width:45px;line-height:2.3"><li>Heart Failure</li><li>Depression</li><li>Diabetes</li><li>Hypertension</li><li>Osteoporosis</li></ul>
  <p class="a white" style="left:17px;top:149px;margin:0;font-size:5.6px;font-weight:500">What is a Chronic Condition?</p>
  <p class="a white tiny" style="left:17px;top:164px;width:95px;margin:0">The Centers for Disease Control and Prevention (CDC) defines a chronic condition as, "Conditions that last 1 year or more and require ongoing medical attention or limit activities of daily living or both. Chronic diseases such as heart disease, cancer, and diabetes are the leading causes of death and disability in the United States."</p>
  <div class="a info-icon" style="left:17px;top:233px"></div>
  <p class="a white" style="left:29px;top:235px;margin:0;font-size:3px">www.healthref.org/chronic-conditions</p>
  <div class="a" role="img" aria-label="Photo of a physician writing notes beside a laptop" style="left:124px;top:53px;width:205px;height:189px;background:linear-gradient(135deg,#eef2f5,#b9c6d0 60%,#7f96a8)"></div>
  <div class="site-head"><span>www.bramforddx.com</span><div class="brand"><i></i>Bramford Diagnostics</div></div>
  <p class="a blue" style="left:333px;top:53px;margin:0;font-size:5px;font-weight:700">PERSONALIZED</p>
  <h2 class="a title" style="left:333px;top:61px;font-size:10.5px;line-height:1.2">Comprehensive<br>Care Plan</h2>
  <p class="a tiny" style="left:333px;top:98px;width:72px;margin:0;color:var(--gray-dark)">First, a member of the patient CCM team will complete a full assessment that includes:</p>
  <div class="a" style="left:333px;top:120px;width:75px">
    <div class="plan-item" style="margin-bottom:12px"><i style="border-radius:50%"></i><span>How is the patient feeling physically and emotionally.</span></div>
    <div class="plan-item" style="margin-bottom:12px"><i style="border-radius:50%"></i><span>Whether patient have access to resources like food, transportation and/or medications.</span></div>
    <div class="plan-item"><i style="border-radius:50%"></i><span>A review of all the medications patient is taking and how patient is taking them.</span></div>
  </div>
  <div class="folio l" style="background:var(--gray-dark)"></div><div class="folio r"></div>
</section>

<!-- ===== Row 3 : Care plan activities / CCM vs Complex ===== -->
<section class="spread" style="left:470px;top:607px">
  <div class="a" role="img" aria-label="Photo of a nurse in blue scrubs caring for an older patient" style="left:0;top:0;width:209px;height:97px;background:linear-gradient(100deg,#f1ede6,#cfd7dc 55%,#7fb6d9)"></div>
  <p class="a" style="left:22px;top:109px;width:170px;margin:0;font-size:3.8px;font-weight:500;color:var(--ink);line-height:1.3">Once the assessment is complete, the CCM team will create a plan that helps patient with specific activities each month such as:</p>
  <div class="a" style="left:22px;top:127px;width:82px">
    <div class="plan-item"><i></i><span>Ensuring patient are up-to-date and active with patient medications.</span></div>
    <div class="plan-item"><i></i><span>Facilitating communication between all of patient health-care providers.</span></div>
    <div class="plan-item"><i></i><span>Offering tips and techniques on how to deal with problems associated with chronic health conditions like pain, fatigue, frustration and getting a good night's sleep.</span></div>
  </div>
  <div class="a" style="left:108px;top:127px;width:86px">
    <div class="plan-item"><i></i><span>Helping patien connect with community resources.</span></div>
    <div class="plan-item"><i></i><span>Assisting with goal-setting, problem solving and overcoming barriers.</span></div>
    <div class="plan-item"><i></i><span>Providing resources to help patient better manage his or her symptoms.</span></div>
  </div>
  <div class="a bg-blue" style="left:0;top:211px;width:209px;height:60px"></div>
  <div class="a info-icon" style="left:32px;top:230px"></div>
  <p class="a white" style="left:45px;top:230px;width:150px;margin:0;font-size:3.2px;font-style:italic;line-height:1.35">Overall, CCM helps you take an active role in patient care.<br>It increases the likelihood that patient will get healthier and moves patient closer to achieving patient health-care goals.</p>
  <div class="a bg-gray" style="left:209px;top:34px;width:209px;height:237px"></div>
  <div class="site-head"><span>www.bramforddx.com</span><div class="brand"><i></i>Bramford Diagnostics</div></div>
  <h2 class="a white cond" style="left:232px;top:47px;margin:0;font-size:6.5px">CCM vs. Complex CCM</h2>
  <p class="a white tiny" style="left:232px;top:58px;width:168px;margin:0">There are two different types of CCM. Classic chronic care management and complex chronic care management. Standard CCM can be distinguished from complex CCM by the respective CPT code. Complex CCM uses codes 99487 and 99489. Complex CCM patients' care teams must have a significant establishment or revision of the care plan and typically communicate more with the care team staff in a calendar month.</p>
  <table class="a codes">
    <thead><tr><th style="width:20%">Billing Code</th><th style="width:15%">Code Description</th><th>Summary Requirements</th><th style="width:14%">Average Payment</th></tr></thead>
    <tbody>
      <tr style="height:24px"><td>HCPCS G0506</td><td>Comprehensive Assessment &amp; Care Planning</td><td><ul><li>Patient enrolled in person</li><li>Systematic assessment &amp; care planning personally performed by the billing provider</li><li>Add-on code to the standard E/M code. AWV or IPPE initiating visit</li></ul></td><td>$63</td></tr>
      <tr style="height:21px"><td>CPT 99490</td><td>Standard CCM</td><td><ul><li>20+ minutes of care management outside of office visits performed by clinical staff</li><li>Care plan established and regularly reviewed</li></ul></td><td>64.07</td></tr>
      <tr style="height:20px"><td>CPT 99439</td><td>Non-Complex Add-on</td><td><ul><li>Additional 20 minutes of "non-complex" CCM</li><li>Reportable up to 2x per month (after 99490)</li></ul></td><td>48.17</td></tr>
      <tr style="height:23px"><td>CPT 99487</td><td>Complex CCM</td><td><ul><li>60+ minutes of care management outside office visits</li><li>Care plan created and / or significantly revised</li></ul></td><td>$134.27</td></tr>
      <tr style="height:24px"><td>CPT 99489</td><td>Complex Add-on</td><td><ul><li>Billed incrementally for each additional 30 minutes spent beyond the first 60 minutes for Complex CCM case</li></ul></td><td>$70.60</td></tr>
    </tbody>
  </table>
  <div class="folio l" style="background:var(--gray-dark)"></div><div class="folio r"></div>
</section>

<!-- ===== Row 4 : Patient scenarios ===== -->
<section class="spread" style="left:35px;top:897px">
  <p class="a" style="left:20px;top:35px;margin:0;font-size:5px;font-weight:700;color:var(--gray-dark)">PROFESSIONAL RESOURCE</p>
  <h2 class="a cond" style="left:20px;top:43px;margin:0;font-size:9.5px;line-height:1.25;color:var(--gray-dark)">Chronic Care<br>Management</h2>
  <h2 class="a title" style="left:20px;top:79px;font-size:9.5px">Patient Scenarios</h2>
  <p class="a tiny" style="left:20px;top:109px;width:96px;margin:0;color:var(--gray-dark)">Chronic Care Management (CCM) offers personal support to patients with complex needs. This added level of care and service leads patients to a healthier lifestyle by proactively managing their care and providing a trusted clinical resource they can reach around-the-clock. CCM is designed for patients with two or more chronic conditions that are anticipated to last at least 12 months or until the patient's death. Patients enrolled in CCM services benefit from an entire care team focused on their needs, increased communication with their provider and improved care coordination.</p>
  <div class="a bg-blue" style="left:124px;top:0;width:85px;height:168px"></div>
  <div class="a info-icon" style="left:165px;top:98px;width:10px;height:10px;line-height:10px;font-size:6px"></div>
  <p class="a white" style="left:134px;top:117px;width:68px;margin:0;font-size:3.1px;font-style:italic;line-height:1.4">The patient scenarios below help demonstrate how CCM services and billing work on a monthly basis. Reference the chart to find the correct billing code for each example</p>
  <div class="scenario orange" style="left:21px;top:182px;width:171px">
    <div class="bar">SAMPLE PATIENT ONE: Liam • 67 years old • Medicare</div>
    <div class="desc">Liam has been diagnosed with Type 2 diabetes and hypertension<br>Liam began CCM services at his Medicare Annual Wellness Visit</div>
    <div class="cols"><span>Activity Log</span><span>Time Spent</span></div>
    <div class="row"><div>A nurse calls Liam two days after his E&amp;M visit and discusses lab results</div><div class="t no">10 minutes</div><div class="m">MONTH</div></div>
    <div class="row"><div>Liam calls his CCM nurse with blood sugar levels and question</div><div class="t">20 minutes</div><div class="m">ONE</div></div>
    <div class="row bill"><div>CCM Billing • Bill 99490 (non-complex CCM) for month one</div><div class="t">20 minutes • Bill 99490</div><div></div></div>
    <div class="note">NOTE: The 10-minute phone call Liam makes to his nurse counts for CCM. However, the 10-minute call the nurse made does not count because it was related to the E&amp;M visit.</div>
  </div>
  <div class="site-head"><span>www.bramforddx.com</span><div class="brand"><i></i>Bramford Diagnostics</div></div>
  <div class="scenario orange" style="left:224px;top:29px;width:177px">
    <div class="bar">SAMPLE PATIENT ONE: Liam • 67 years old • Medicare</div>
    <div class="desc">Liam has been diagnosed with Type 2 diabetes and hypertension<br>Liam began CCM services at his Medicare Annual Wellness Visit</div>
    <div class="cols"><span>Activity Log</span><span>Time Spent</span></div>
    <div class="row"><div>The CCM nurse calls Liam to discuss diet education</div><div class="t">10 minutes</div><div class="m">MONTH</div></div>
    <div class="row"><div>The CCM nurse calls Liam to discuss blood sugar review</div><div class="t">7 minutes</div><div class="m">TWO</div></div>
    <div class="row bill"><div>CCM Billing • CANNOT BILL for month one</div><div class="t no">17 minutes • Cannot Bill</div><div></div></div>
    <div class="note">NOTE: Unable to bill for CCM because the time spent was less than 20 minutes.</div>
    <div class="row"><div>The CCM nurse corresponds with Liam via email about his blood sugar</div><div class="t">25 minutes</div><div class="m">MONTH</div></div>
    <div class="row"><div>The CCM nurse calls Liam to discuss blood pressure review</div><div class="t">10 minutes</div><div class="m">THREE</div></div>
    <div class="row bill"><div>CCM Billing • Bill 99490 (non-complex CCM) for month three</div><div class="t">35 minutes • Bill 99490</div><div></div></div>
  </div>
  <div class="scenario" style="left:224px;top:117px;width:177px">
    <div class="bar">SAMPLE PATIENT TWO: Amelia • 72 years old • Medicare</div>
    <div class="desc">Amelia has been diagnosed with Congestive Heart Failure, Chronic Obstructive Pulmonary Disease and Hypertension. She recently was hospitalized with CHF and COPD exacerbation. Amelia's chronic issues and recent hospitalization requires moderate or high complexity medical decision making.</div>
    <div class="cols"><span>Activity Log</span><span>Time Spent</span></div>
    <div class="row"><div>Amelia is billed for transitional care management after returning from the hospital</div><div class="t">30 minutes</div><div class="m">MONTH</div></div>
    <div class="row"><div>The CCM nurse calls Amelia and she gives consent to start CCM services</div><div class="t no">10 minutes</div><div class="m">ONE</div></div>
    <div class="row bill"><div>CCM Billing • CANNOT BILL for month one</div><div class="t no">0 minutes • Cannot Bill</div><div></div></div>
    <div class="note">NOTE: Bill for Code 99495 (transitional care management). CCM code cannot be billed in the same month as TCM.</div>
    <div class="row"><div>Amelia calls her CCM nurse and discusses her questions concerning salt in her diet</div><div class="t">10 minutes</div><div class="m">MONTH</div></div>
    <div class="row"><div>The CCM nurse made calls coordinating Amelia's care with her PCP, Cardiology and Pulmonology providers and updates her care plan</div><div class="t">30 minutes</div><div class="m">TWO</div></div>
    <div class="row"><div>The CCM nurse calls Amelia and completes medication reconciliation</div><div class="t">20 minutes</div><div></div></div>
    <div class="row"><div>Amelia calls the CCM nurse to discuss care to prevent her having to go to the hospital</div><div class="t">30 minutes</div><div></div></div>
    <div class="row bill"><div>CCM Billing • Bill 99487 (complex CCM) for month two</div><div class="t">90 minutes • Bill 99487 + 99489</div><div></div></div>
    <div class="note">NOTE: Since there was a total of 90 minutes of CCM services, add 99489 when billing for the additional 30 minutes of complex CCM services.</div>
  </div>
  <div class="folio l"></div><div class="folio r"></div>
</section>

<!-- ===== Row 4 : Scenarios / Featured products ===== -->
<section class="spread" style="left:470px;top:897px">
  <div class="scenario" style="left:17px;top:33px;width:177px">
    <div class="bar">SAMPLE PATIENT TWO: Amelia • 72 years old • Medicare</div>
    <div class="desc">Amelia has been diagnosed with Congestive Heart Failure, Chronic Obstructive Pulmonary Disease and Hypertension. She recently was hospitalized with CHF and COPD exacerbation. Amelia's chronic issues and recent hospitalization requires moderate or high complexity medical decision making.</div>
    <div class="cols"><span>Activity Log</span><span>Time Spent</span></div>
    <div class="row"><div>The CCM nurse runs and reviews several reports to schedule patients for immunizations and check-ups. Amelia is on two of the lists for needed immunizations</div><div class="t no">30 minutes</div><div class="m">MONTH</div></div>
    <div class="row"><div>The receptionist contacts Amelia and schedules immunizations</div><div class="t no">10 minutes</div><div class="m">THREE</div></div>
    <div class="row"><div>The CCM nurse calls Amelia and reviews her most recent blood pressure readings</div><div class="t">15 minutes</div><div></div></div>
    <div class="row bill"><div>CCM Billing • CANNOT BILL for month three</div><div class="t no">15 minutes • Cannot Bill</div><div></div></div>
    <div class="note">NOTE: CCM cannot be billed this month because only 15 of the 25 minutes spent was by an appropriate CCM provider. The time spent running reports for immunizations does not count as CCM time because it was not specific to Amelia. The time spent scheduling immunizations does not count because receptionists cannot perform CCM services.</div>
  </div>
  <div class="scenario" style="left:17px;top:136px;width:177px">
    <div class="bar">SAMPLE PATIENT THREE: Jose • 66 years old • Medicare</div>
    <div class="desc">Jose has been diagnosed with Rheumatoid Arthritis (RA) and Asthma.<br>Jose began CCM services at his Medicare Annual Wellness Visit</div>
    <div class="cols"><span>Activity Log</span><span>Time Spent</span></div>
    <div class="row"><div>The CCM nurse speaks with Jose over the phone about a new asthma inhaler</div><div class="t">10 minutes</div><div class="m">MONTH</div></div>
    <div class="row"><div>Dr. Smith calls Jose to discuss a new RA medication that she would like Jose to try</div><div class="t">20 minutes</div><div class="m">ONE</div></div>
    <div class="row"><div>Dr. Smith coordinates the prescription, completes medication reconciliation and medication delivery with the pharmacist for the new RA medication for Jose</div><div class="t">15 minutes</div><div></div></div>
    <div class="row bill"><div>CCM Billing • BILL 99491 for month one</div><div class="t">5 minutes • Bill 99491</div><div></div></div>
    <div class="note">NOTE: 99491 is billed because the MD spent a minimum of 30 minutes on non-face to face CCM services in month one.</div>
  </div>
  <div class="a bg-blue" style="left:17px;top:235px;width:177px;height:11px"></div>
  <p class="a white" style="left:25px;top:238px;margin:0;font-size:3.3px">www.bramforddx.com</p>
  <div class="a bg-gray" style="left:209px;top:49px;width:209px;height:222px"></div>
  <div class="site-head"><span>www.bramforddx.com</span><div class="brand"><i></i>Bramford Diagnostics</div></div>
  <h2 class="a title" style="left:229px;top:29px;font-size:14px">Featured Products</h2>
  <p class="a white" style="left:231px;top:58px;margin:0;font-size:5.6px;font-weight:500">Hub Solution</p>
  <p class="a white" style="left:231px;top:65px;margin:0;font-size:3px">Open solution, unlimited scalability.</p>
  <svg class="a" style="left:229px;top:72px" width="180" height="45" viewBox="0 0 180 45" role="img" aria-label="Diagram of a monitoring hub connecting patient devices to a device management dashboard">
    <g fill="none" stroke="#e8a25a" stroke-width=".4"><line x1="40" y1="12" x2="92" y2="12"/><line x1="110" y1="12" x2="150" y2="12"/><line x1="101" y1="18" x2="101" y2="34"/><line x1="101" y1="34" x2="160" y2="34"/><line x1="150" y1="4" x2="150" y2="22"/></g>
    <rect x="14" y="3" width="26" height="17" fill="#ffffff"/><rect x="14" y="3" width="26" height="3" fill="var(--blue)"/>
    <ellipse cx="101" cy="13" rx="10" ry="4" fill="#ffffff"/>
    <g font-family="Roboto,sans-serif" font-size="2.3" fill="#ffffff"><text x="12" y="25">Device management dashboard</text><text x="62" y="10">Data transmission</text><text x="120" y="8">Integrated easily</text><text x="92" y="38">Connection</text><text x="150" y="38">Legacy devices</text></g>
    <g fill="#e8a25a" font-family="Roboto,sans-serif" font-size="2"><text x="140" y="2">Open to any platform</text></g>
  </svg>
  <div class="a" role="img" aria-label="Row of small connected health devices: blood pressure cuff, scale, glucose meter, watch" style="left:236px;top:117px;width:160px;height:14px;background:linear-gradient(90deg,#9a9da1,#b8bbbf 50%,#9a9da1);border-radius:2px"></div>
  <div class="a" role="img" aria-label="Photo of hands holding a blood pressure monitor next to an inhaler and thermometer" style="left:231px;top:140px;width:113px;height:47px;background:linear-gradient(135deg,#e8e9eb,#c6c9cd 60%,#9ea3a8)"></div>
  <p class="a white" style="left:350px;top:163px;width:60px;margin:0;font-size:2.8px;line-height:1.4">The Beacon mobile emergency medical system gives a simple to use help button to users at home and away from home.</p>
  <div class="a" role="img" aria-label="Photo of a home emergency response base unit with pendant" style="left:231px;top:193px;width:113px;height:66px;background:linear-gradient(135deg,#f3f4f5,#d5d8db 60%,#adb2b7)"></div>
  <p class="a white" style="left:350px;top:220px;width:60px;margin:0;font-size:2.8px;line-height:1.4">The VitalHome Classic system gives patients access to personal emergency response services plus the benefits of monitoring important aspects of their health.</p>
  <div class="folio l"></div><div class="folio r"></div>
</section>

</main>
</body>
</html>
```